Corporate Brochure for trade show in the Video Surveillance industry

We need a design for this brochure: https://files.examplehost.net/s/7kqpzr2mvtw9xcd/edits_5mQIX%20Deck%20%28Sept%202022%29.pptx?dl=0
Print size: regular 8.5x11 inches, horizontal, number of pages depend on the design.
Need clean and corporate look , similar to this style: https://slides.samplecloud.org/presentation/d/9RtwLm2Xp4QvZs7NbYc3HjDkFg8TuVeA5oWnPyrMxq/edit#slide=id.h4820cc7aef_2_31

Target Market(s)

Security integrators and monitoring stations

Industry/Entity Type

security and video surveillance

Font styles to use
Sans Serif

Colors
00AB8E
00BBA5
67D7C9
C6EFE9
E9F9F6

Requirements
Must have
• print -ready file in the end and editable file in Photoshop

```html
<!DOCTYPE html>
<html lang="en">
<head>
<meta charset="utf-8">
<title>5mQIX Brochure – Pricing &amp; Contact</title>
<link rel="stylesheet" href="https://fonts.googleapis.com/css2?family=Nunito+Sans:wght@400;600;700;800&display=swap">
<style>
  :root {
    --teal-deep: #00AB8E;
    --teal: #00BBA5;
    --teal-light: #67D7C9;
    --teal-pale: #C6EFE9;
    --teal-mist: #E9F9F6;
    --navy: #0f2340;
    --ink: #1c2430;
    --purple: #5a2f86;
    --slate: #3e7c8c;
    --paper: #f7f7f6;
    --backdrop: #d9d9d9;
  }
  * { box-sizing: border-box; margin: 0; padding: 0; }
  html, body { width: 1200px; height: 641px; overflow: hidden; }
  body {
    background: var(--backdrop);
    font-family: "Nunito Sans", Arial, sans-serif;
    color: var(--ink);
    position: relative;
  }
  .spread {
    position: absolute;
    left: 20px; top: 90px;
    width: 1160px; height: 462px;
    display: flex;
  }
  .page { position: relative; width: 580px; height: 462px; overflow: hidden; }

  /* Pricing page */
  .page--pricing { background: linear-gradient(90deg, #efefed 0%, var(--paper) 60%, #fbfbfa 100%); }
  .wave-field {
    position: absolute; left: 50px; top: 10px; width: 480px; height: 420px;
    background: radial-gradient(ellipse at 40% 50%, rgba(103,215,201,0.10), rgba(103,215,201,0) 70%);
  }
  .pricing__title {
    position: absolute; left: 99px; top: 53px;
    font-size: 17.5px; font-weight: 800; letter-spacing: 0.5px; color: var(--navy);
  }
  .band {
    position: absolute; left: 62px; right: 6px;
    background: linear-gradient(90deg, #1faa8d 0%, #24ae92 55%, #7dd6c6 82%, #2fc3a7 100%);
    color: #fff; font-size: 8.4px; letter-spacing: 0.4px; line-height: 1.6;
    padding-left: 52px; padding-right: 70px;
    display: flex; align-items: center;
  }
  .band::before {
    content: ""; position: absolute; left: 37px; width: 4px; height: 4px;
    border-radius: 50%; background: #fff; top: 50%; margin-top: -6px;
  }
  .band--model { top: 81px; height: 45px; }
  .band--terms { top: 284px; height: 55px; font-size: 8.8px; }
  .feature-list { position: absolute; top: 138px; font-size: 7.6px; letter-spacing: 0.3px; list-style: none; }
  .feature-list__head { color: var(--teal); font-size: 8.4px; margin-bottom: 5px; }
  .feature-list li { height: 17.8px; line-height: 17.8px; }
  .feature-list--included { left: 121px; }
  .feature-list--included li { font-weight: 600; }
  .feature-list--addons { left: 315px; top: 137px; }

  /* Contact page */
  .page--contact { background: #fafafa; }
  .contact-panel {
    position: absolute; left: 0; top: 0; width: 348px; height: 100%;
    background:
      linear-gradient(0deg, rgba(90,47,134,0.85) 0%, rgba(90,47,134,0) 30%),
      linear-gradient(90deg, #2f4f86 0%, var(--slate) 15%, #7bcfbf 50%, var(--teal) 100%);
  }
  .brand-mark {
    position: absolute; left: 300px; top: 145px; width: 130px; height: 130px;
    border-radius: 50%; background: var(--teal);
  }
  .brand-name {
    position: absolute; left: 442px; top: 196px;
    font-size: 24px; font-weight: 800; color: var(--teal-deep);
  }
  .contact__title {
    position: absolute; left: 42px; top: 238px;
    color: #fff; font-size: 13.5px; font-weight: 700; letter-spacing: 1px;
  }
  .contact-item { position: absolute; color: #fff; letter-spacing: 0.5px; }
  .contact-item__label { font-size: 9px; font-weight: 400; opacity: 0.9; }
  .contact-item__value { font-size: 9.5px; font-weight: 800; margin-top: 2px; }
  .contact-item--partners { left: 42px; top: 274px; }
  .contact-item--sales { left: 42px; top: 316px; }
  .contact-item--phone { left: 42px; top: 358px; }
  .contact-item--web { left: 205px; top: 356px; }
</style>
</head>
<body>
<main class="spread">
  <section class="page page--pricing">
    <div class="wave-field" role="img" aria-label="Faint flowing teal line pattern"></div>
    <h1 class="pricing__title">PRICING</h1>
    <p class="band band--model">Pay-as-you-go pricing: fixed subscription per camera per month or billed for total network consumption per TB/month;</p>
    <ul class="feature-list feature-list--included">
      <li class="feature-list__head">Included in monthly pay-as-you-go:</li>
      <li>- Unlimited updates</li>
      <li>- Plug &amp; Play integrations</li>
      <li>- Alarm Station module</li>
      <li>- Billing Module</li>
      <li>- Remote administrative tools</li>
      <li>- Clips and time-lapses storage</li>
      <li>- Co-branding customization</li>
    </ul>
    <ul class="feature-list feature-list--addons">
      <li class="feature-list__head">Optional add-ons:</li>
      <li>- Cloud AI Analytics</li>
      <li>- Long-term time-lapses</li>
      <li>- Broadcasting widget</li>
      <li>- Cloud re-encoding</li>
      <li>- Complete White-Label of web and app portals</li>
    </ul>
    <p class="band band--terms">Lifetime updates, no hidden fees or user restrictions: scale &amp; create unlimited end-users, dealers, and add unlimited cameras.</p>
  </section>

  <section class="page page--contact">
    <div class="contact-panel" role="img" aria-label="Purple to teal gradient with flowing line pattern"></div>
    <div class="brand-mark"></div>
    <div class="brand-name">5mQIX</div>
    <h2 class="contact__title">CONTACT INFORMATION</h2>
    <div class="contact-item contact-item--partners">
      <div class="contact-item__label">Partnerships:</div>
      <div class="contact-item__value">marketing@5mqix.me</div>
    </div>
    <div class="contact-item contact-item--sales">
      <div class="contact-item__label">Sales:</div>
      <div class="contact-item__value">sales@5mqix.me</div>
    </div>
    <div class="contact-item contact-item--phone">
      <div class="contact-item__label">Phone:</div>
      <div class="contact-item__value">+1-800-555-0147 &nbsp;(Toll Free)</div>
    </div>
    <div class="contact-item contact-item--web">
      <div class="contact-item__label">Website:</div>
      <div class="contact-item__value">www.5mqix.me</div>
    </div>
  </section>
</main>
</body>
</html>
```